64 on Birch Apartment Mailer to Competition

I need a postcard mailer designed that will be promoting a new apartment building in downtown Rochester NY. The postcards are being mailed to other apartment communities the we are in direct competition with. I have enclosed a bunch of info to guide you.

Target Market(s)

Other communities in the market

Industry/Entity Type

Property Management

Requirements
Must have
• Exterior rendering, features. Fit standard postcard, colors similar to enclosed, grey, white coral
Nice to have
• Interior Pictures

```html
<!DOCTYPE html>
<html lang="en">
<head>
<meta charset="utf-8">
<title>64 on Birch — Postcard Mailer</title>
<link rel="stylesheet" href="https://fonts.googleapis.com/css2?family=Fira+Sans+Extra+Condensed:wght@400;600&display=swap">
<style>
  :root {
    --coral: #e8423a;
    --maroon: #6e2b28;
    --white: #ffffff;
  }
  * { margin: 0; padding: 0; box-sizing: border-box; }
  html, body { width: 1200px; height: 850px; overflow: hidden; background: var(--white); }
  .mailer {
    position: relative;
    width: 1200px;
    height: 850px;
    overflow: hidden;
    background: var(--white);
    font-family: "Fira Sans Extra Condensed", "Arial Narrow", sans-serif;
  }
  .mailer-art { position: absolute; inset: 0; }
  .brand {
    position: absolute;
    left: 0; top: 26px;
    width: 256px; height: 152px;
    display: flex; align-items: center; justify-content: center; gap: 10px;
  }
  .brand-mark { width: 18px; height: 18px; border-radius: 50%; background: var(--coral); }
  .brand-name {
    font-weight: 400;
    font-size: 32px;
    color: var(--coral);
  }
  .contact { position: absolute; left: 38px; top: 474px; color: var(--white); }
  .contact-heading {
    font-weight: 600;
    font-size: 42px;
    line-height: 48px;
    text-transform: uppercase;
  }
  .contact-phone {
    font-weight: 600;
    font-size: 62px;
    line-height: 66px;
    color: var(--coral);
    margin-top: 2px;
  }
  .contact-line {
    font-size: 36px;
    line-height: 44px;
  }
  .contact-line:first-of-type { margin-top: 2px; }
  .social {
    font-size: 24px;
    line-height: 28px;
    margin-top: 8px;
  }
</style>
</head>
<body>
<main class="mailer">
  <svg class="mailer-art" width="1200" height="850" viewBox="0 0 1200 850">
    <defs>
      <linearGradient id="exteriorTone" x1="0" y1="0" x2="1" y2="1">
        <stop offset="0" stop-color="#7a332f"/>
        <stop offset="0.5" stop-color="#6e2b28"/>
        <stop offset="1" stop-color="#5c2421"/>
      </linearGradient>
      <linearGradient id="kitchenTone" x1="0" y1="0" x2="1" y2="1">
        <stop offset="0" stop-color="#b9b3aa"/>
        <stop offset="0.6" stop-color="#8d857b"/>
        <stop offset="1" stop-color="#3f3530"/>
      </linearGradient>
      <linearGradient id="bathTone" x1="0" y1="0" x2="1" y2="1">
        <stop offset="0" stop-color="#a59e92"/>
        <stop offset="0.5" stop-color="#7d7568"/>
        <stop offset="1" stop-color="#b3b0aa"/>
      </linearGradient>
      <clipPath id="panelShape">
        <path d="M0 0 H600 C672 120 676 420 352 850 H0 Z"/>
      </clipPath>
    </defs>

    <path class="panel-edge" d="M0 0 H618 C694 120 694 430 372 850 H0 Z" fill="var(--coral)"/>

    <g clip-path="url(#panelShape)">
      <rect class="exterior-rendering" x="0" y="0" width="700" height="850" fill="url(#exteriorTone)"
            role="img" aria-label="Exterior rendering of the apartment building with a red tint"/>
      <rect class="interior-band" x="0" y="202" width="700" height="248" fill="var(--coral)"/>
      <rect class="interior-kitchen" x="0" y="212" width="309" height="226" fill="url(#kitchenTone)"
            role="img" aria-label="Apartment kitchen with granite island, bar stools and stainless appliances"/>
      <rect class="interior-bath" x="318" y="212" width="322" height="226" fill="url(#bathTone)"
            role="img" aria-label="Apartment bathroom with vanity, mirror and glass tile shower"/>
    </g>

    <rect class="brand-pill" x="-40" y="26" width="296" height="152" rx="76" fill="var(--white)"
          stroke="var(--coral)" stroke-width="5"/>
  </svg>

  <div class="brand">
    <span class="brand-mark"></span>
    <span class="brand-name">64 on Birch</span>
  </div>

  <section class="contact">
    <h1 class="contact-heading">Call today<br>for information</h1>
    <p class="contact-phone">585.555.0164</p>
    <p class="contact-line">LEASING@64ONBIRCH.COM</p>
    <p class="contact-line">WWW.64ONBIRCH.COM</p>
    <p class="social">Follow us AT<br>Linkway.com/64onBirch or on<br>SNAPLY @64_on_BIRCH</p>
  </section>
</main>
</body>
</html>
```